New Business Card Design for Manufacturing

We are an engineering/manufacturing company that offers Advanced machining/assembly/engineering services, as well as innovative products for the heavy duty engine cooling markets.

We are looking to get a new business card designed that is clean and modern looking, but still fits the wide range of technical/skilled work we do.

- We hope to use this design as the base for other design work in new Presentations, web, and print work.

Industry/Entity Type

Engineering

Contact Information for Business Card

Our preferred color of blue is (RGB) 22/71/159 but can vary slightly from that color. Our content will be our Logo and full company name (Fabricated Tooling Works, Inc.), company address, name, job title, phone number with extension, cell number, fax number, website, and email address on the cards.
We'd like the full company name next to the logo, but we are open to other interpretations of that layout.
Preferably, we would like the back side to be clean with just our logo, and the front to contain all of the contact information.

Colors
2f74b4
0355a3
85abd2

Requirements
Must have
• - Logo, company name, needed content - We are open to interpretation beyond that.
• - Standard size business card.
• - Horizontal orientation.
• - Enough space for lengthy names / job titles (for example, a job title could read "Directory of Human Resources" or "V.P. of Governmental Affairs"). We need this to look clean, whether the title be short (CEO) or long (as described above).

```html
<!DOCTYPE html>
<html lang="en">
<head>
<meta charset="utf-8">
<title>Fabricated Tooling Works – Business Card</title>
<link href="https://fonts.googleapis.com/css2?family=Roboto+Condensed:wght@400;700&display=swap" rel="stylesheet">
<style>
  :root {
    --backdrop: #2b2b2d;
    --card-black: #0b0b0c;
    --card-sheen: #2a2a2c;
    --brand-blue: #1647a0;
    --brand-bright: #2f74b4;
    --stripe-grey: #b9bcc2;
    --ink-white: #ffffff;
  }
  * { margin: 0; padding: 0; box-sizing: border-box; }
  html, body { width: 1200px; height: 896px; overflow: hidden; }
  body {
    background: var(--backdrop);
    font-family: "Roboto Condensed", "Arial Narrow", sans-serif;
    position: relative;
  }
  .card {
    position: absolute;
    width: 540px;
    height: 309px;
    border-radius: 26px;
    overflow: hidden;
    background: linear-gradient(160deg, var(--card-sheen) 0%, var(--card-black) 45%, var(--card-black) 100%);
    box-shadow: 0 18px 40px rgba(0,0,0,.55);
  }
  .card--back { left: 60px; top: 110px; }
  .card--front { left: 600px; top: 477px; }

  .brand-name {
    position: absolute;
    color: var(--brand-bright);
    font-weight: 700;
    white-space: nowrap;
    letter-spacing: .3px;
  }
  .card--back .brand-name { left: 70px; top: 138px; font-size: 26px; }
  .card--front .brand-name { left: 28px; top: 144px; font-size: 15px; }

  .back__web {
    position: absolute;
    right: 40px;
    bottom: 40px;
    color: var(--ink-white);
    font-size: 15px;
    letter-spacing: .5px;
  }
  .back__web span { color: var(--brand-bright); }

  .front__panel { position: absolute; inset: 0; }

  .contact {
    position: absolute;
    left: 305px;
    top: 44px;
    color: var(--ink-white);
  }
  .contact__name {
    font-weight: 700;
    font-size: 24px;
    letter-spacing: .5px;
    text-transform: uppercase;
  }
  .contact__title { font-size: 13px; margin-top: 2px; }
  .contact__address { font-size: 13px; margin-top: 14px; line-height: 1.4; }
  .contact__lines { list-style: none; margin-top: 14px; font-size: 13px; line-height: 1.55; }
  .contact__lines li { display: flex; align-items: center; gap: 6px; }
  .contact__lines svg { width: 11px; height: 11px; flex: none; }
</style>
</head>
<body>

<section class="card card--back" aria-label="Business card back">
  <div class="brand-name">Fabricated Tooling Works, Inc.</div>
  <div class="back__web">www.<span>fabtoolworks</span>.com</div>
</section>

<section class="card card--front" aria-label="Business card front">
  <svg class="front__panel" viewBox="0 0 540 309" width="540" height="309" aria-hidden="true">
    <path d="M300 0 C230 70 215 210 238 309 L540 309 L540 0 Z" fill="var(--brand-blue)"/>
    <path d="M318 0 C250 70 236 210 258 309 L540 309 L540 0 Z" fill="var(--stripe-grey)"/>
    <path d="M330 0 C262 70 249 210 271 309 L540 309 L540 0 Z" fill="var(--brand-blue)"/>
  </svg>

  <div class="brand-name">Fabricated Tooling Works, Inc.</div>

  <div class="contact">
    <div class="contact__name">Dana Whitfield</div>
    <div class="contact__title">Directory of Human Resources</div>
    <div class="contact__address">418 Harlan Ave., Ste. 210<br>Columbus, OH 43215 USA</div>
    <ul class="contact__lines">
      <li>(555) 214-3068
        <svg viewBox="0 0 12 12"><path d="M3 1 L5 3.5 L4 5 C4.8 6.6 5.6 7.4 7 8 L8.5 7 L11 9 L9.8 11 C5.5 10.6 1.5 6.5 1 2.2 Z" fill="var(--ink-white)"/></svg>
      </li>
      <li>info@fabtoolworks.com
        <svg viewBox="0 0 12 12"><rect x="1" y="2.5" width="10" height="7" fill="none" stroke="var(--ink-white)" stroke-width="1.2"/><path d="M1 2.5 L6 6.5 L11 2.5" fill="none" stroke="var(--ink-white)" stroke-width="1.2"/></svg>
      </li>
      <li>www.fabtoolworks.com
        <svg viewBox="0 0 12 12"><circle cx="6" cy="6" r="5" fill="none" stroke="var(--ink-white)" stroke-width="1.1"/><ellipse cx="6" cy="6" rx="2.2" ry="5" fill="none" stroke="var(--ink-white)" stroke-width="1"/><path d="M1 6 H11" stroke="var(--ink-white)" stroke-width="1"/></svg>
      </li>
    </ul>
  </div>
</section>

</body>
</html>
```